I desire to create new signs to be used for general promotion (truck sides, billboards, contract backgrounds)

The center of the sign must be our existing logo, with extensions from that logo to our product types.

Center Logo: VoltNest
surrounding extensions: Electrical Service, Solar Power, EV Charger, and Energy Monitor (each with a descriptive image)
(see attached draft for concept)

Below the image must be an option for one of the following:
318-455-2093 lic 532918
or
517-364-8820 lic 532918

Target Market(s)

homeowners, families, casual commercial

Industry/Entity Type

Electrical

Requirements
Must have
• Must communicate concept completely by image, words are just for clarity.
Should not have
• I like cartoon type images, but not goofy.
Limit number of colors. Bright colors are better.

```html
<!DOCTYPE html>
<html lang="en">
<head>
<meta charset="utf-8">
<title>VoltNest Energy Solutions – Promotional Sign</title>
<link rel="stylesheet" href="https://fonts.googleapis.com/css2?family=Open+Sans:wght@600;700;800&display=swap">
<style>
  :root {
    --navy: #005275;
    --navy-dark: #0d4a6b;
    --yellow: #f0ff00;
    --yellow-shade: #d6e400;
    --orange: #f7941d;
    --white: #ffffff;
    --canvas: #ffffff;
  }
  html, body {
    margin: 0;
    padding: 0;
    width: 1200px;
    height: 900px;
    overflow: hidden;
    background: var(--canvas);
  }
  .canvas {
    position: relative;
    width: 1200px;
    height: 900px;
  }
  .sign {
    position: absolute;
    left: 135px;
    top: 104px;
    width: 940px;
    height: 433px;
    display: block;
  }
  .band { fill: var(--navy); }
  .field { fill: var(--yellow); }
  .icon-stroke { fill: none; stroke: var(--navy); stroke-linecap: round; stroke-linejoin: round; }
  .icon-fill { fill: var(--navy); }
  .service-label {
    font-family: "Open Sans", sans-serif;
    font-weight: 700;
    font-size: 10.5px;
    fill: var(--navy-dark);
  }
  .brand-name {
    font-family: "Open Sans", sans-serif;
    font-weight: 800;
    font-size: 64px;
    fill: var(--navy);
    letter-spacing: -1px;
  }
  .contact-line {
    font-family: "Open Sans", sans-serif;
    font-weight: 700;
    font-size: 14.5px;
    fill: var(--white);
  }
  .connector { fill: none; stroke-width: 1.2; }
</style>
</head>
<body>
<main class="canvas">
  <svg class="sign" viewBox="0 0 940 433" xmlns="http://www.w3.org/2000/svg" aria-labelledby="sign-title">
    <title id="sign-title">VoltNest Energy Solutions – Electrical Service, Solar Power, EV Charger, Energy Monitoring</title>
    <defs>
      <radialGradient id="dome-tone" cx="50%" cy="100%" r="75%">
        <stop offset="0%" stop-color="#cbd800"/>
        <stop offset="100%" stop-color="#dfee00"/>
      </radialGradient>
      <linearGradient id="spotlight" x1="0" y1="0" x2="0" y2="1">
        <stop offset="0%" stop-color="#ffffff" stop-opacity="0.55"/>
        <stop offset="100%" stop-color="#ffffff" stop-opacity="0.05"/>
      </linearGradient>
      <linearGradient id="wire-left" x1="0" y1="0" x2="1" y2="0">
        <stop offset="0%" stop-color="#3f6f8f"/>
        <stop offset="100%" stop-color="#ffffff"/>
      </linearGradient>
      <linearGradient id="wire-right" x1="1" y1="0" x2="0" y2="0">
        <stop offset="0%" stop-color="#3f6f8f"/>
        <stop offset="100%" stop-color="#ffffff"/>
      </linearGradient>
    </defs>

    <!-- field and bands -->
    <rect class="field" x="0" y="21" width="940" height="392"/>
    <g role="img" aria-label="Faint globe dome rising behind the brand name">
      <ellipse cx="470" cy="470" rx="380" ry="300" fill="url(#dome-tone)"/>
    </g>
    <polygon points="420,21 520,21 560,225 380,225" fill="url(#spotlight)"/>
    <ellipse cx="470" cy="225" rx="95" ry="18" fill="#ffffff" opacity="0.35"/>
    <rect class="band" x="0" y="0" width="940" height="21"/>
    <rect class="band" x="0" y="413" width="940" height="20"/>

    <!-- connectors -->
    <g class="connectors">
      <path class="connector" stroke="url(#wire-left)" d="M230 175 C280 180 300 215 345 222"/>
      <path class="connector" stroke="url(#wire-left)" d="M232 179 C282 190 300 222 345 226"/>
      <path class="connector" stroke="url(#wire-left)" d="M234 172 C284 176 306 208 345 218"/>
      <path class="connector" stroke="url(#wire-left)" d="M225 296 C270 296 300 250 345 246"/>
      <path class="connector" stroke="url(#wire-left)" d="M225 300 C275 302 305 260 345 252"/>
      <path class="connector" stroke="url(#wire-left)" d="M225 292 C268 288 298 244 345 240"/>
      <path class="connector" stroke="url(#wire-right)" d="M712 175 C665 180 640 215 600 222"/>
      <path class="connector" stroke="url(#wire-right)" d="M710 179 C662 190 640 222 600 226"/>
      <path class="connector" stroke="url(#wire-right)" d="M708 172 C660 176 636 208 600 218"/>
      <path class="connector" stroke="url(#wire-right)" d="M740 300 C690 300 650 252 600 246"/>
      <path class="connector" stroke="url(#wire-right)" d="M740 304 C690 306 648 260 600 252"/>
      <path class="connector" stroke="url(#wire-right)" d="M740 296 C692 292 652 244 600 240"/>
    </g>

    <!-- energy monitoring icon -->
    <g class="service service-monitoring">
      <path class="icon-stroke" stroke-width="3" d="M145 50 V138 H258"/>
      <path class="icon-stroke" stroke-width="2" d="M139 65 H151 M139 85 H151 M139 105 H151 M139 125 H151"/>
      <path class="icon-stroke" stroke-width="3.5" d="M152 112 L178 85 L196 102 L222 72 L240 62"/>
      <path class="icon-fill" d="M236 54 L250 58 L241 69 Z"/>
      <circle class="icon-stroke" stroke-width="7" cx="210" cy="108" r="10"/>
      <circle class="icon-stroke" stroke-width="6" cx="236" cy="116" r="8"/>
      <text class="service-label" x="197" y="161" text-anchor="middle">Energy Monitoring</text>
      <text class="service-label" x="197" y="175" text-anchor="middle">&amp; Automation</text>
    </g>

    <!-- electrical service icon -->
    <g class="service service-electrical">
      <path class="icon-stroke" stroke-width="3" d="M763 48 V64 M733 60 L743 72 M793 60 L783 72 M713 90 H732 M794 90 H813 M725 120 L738 110 M801 120 L788 110"/>
      <path class="icon-stroke" stroke-width="3" d="M749 124 C749 110 740 106 740 93 A23 23 0 0 1 786 93 C786 106 777 110 777 124 Z"/>
      <path class="icon-stroke" stroke-width="2" d="M755 122 L760 98 L766 98 L771 122"/>
      <rect class="icon-fill" x="751" y="127" width="24" height="5" rx="2"/>
      <rect class="icon-fill" x="753" y="134" width="20" height="5" rx="2"/>
      <rect class="icon-fill" x="758" y="141" width="10" height="4" rx="2"/>
      <text class="service-label" x="760" y="175" text-anchor="middle">Electrical Service</text>
    </g>

    <!-- EV charger icon -->
    <g class="service service-ev">
      <path class="icon-fill" d="M92 262 C96 240 110 232 135 232 C160 232 174 240 178 262 L186 272 V318 H84 V272 Z"/>
      <path fill="#ffffff" d="M104 262 C107 248 116 244 135 244 C154 244 163 248 166 262 Z"/>
      <circle fill="#ffffff" cx="102" cy="284" r="7"/>
      <circle fill="#ffffff" cx="168" cy="284" r="7"/>
      <rect fill="#ffffff" x="120" y="300" width="30" height="4" rx="2"/>
      <rect class="icon-fill" x="88" y="316" width="18" height="18" rx="3"/>
      <rect class="icon-fill" x="164" y="316" width="18" height="18" rx="3"/>
      <path class="icon-stroke" stroke-width="3" d="M186 294 H200"/>
      <rect class="icon-fill" x="200" y="286" width="14" height="16" rx="3"/>
      <path class="icon-stroke" stroke-width="3" d="M214 290 H222 M214 298 H222"/>
      <text class="service-label" x="134" y="350" text-anchor="middle">EV Charger</text>
    </g>

    <!-- solar power icon -->
    <g class="service service-solar">
      <polygon class="icon-fill" points="770,222 842,218 836,290 762,292"/>
      <g fill="#ffffff">
        <polygon points="775,227 796,226 795,248 773,249"/>
        <polygon points="800,226 818,225 817,247 799,248"/>
        <polygon points="822,225 837,224 836,246 821,247"/>
        <polygon points="773,253 795,252 794,274 771,275"/>
        <polygon points="799,252 817,251 816,273 798,274"/>
        <polygon points="821,251 836,250 835,272 820,273"/>
      </g>
      <g class="icon-fill">
        <polygon points="777,229 794,228 793,246 775,247"/>
        <polygon points="802,228 816,227 815,245 801,246"/>
        <polygon points="824,227 835,226 834,244 823,245"/>
        <polygon points="775,255 793,254 792,272 773,273"/>
        <polygon points="801,254 815,253 814,271 800,272"/>
        <polygon points="823,253 834,252 833,270 822,271"/>
      </g>
      <path class="icon-stroke" stroke-width="4" d="M800 292 V318"/>
      <path class="icon-fill" d="M770 326 C780 314 820 314 832 326 Z"/>
      <text class="service-label" x="800" y="341" text-anchor="middle">Solar Power</text>
    </g>

    <!-- brand name -->
    <text class="brand-name" x="470" y="285" text-anchor="middle">VoltNest</text>

    <!-- contact band -->
    <text class="contact-line" x="2" y="428">318-455-2093 lic 532918</text>
    <text class="contact-line" x="938" y="428" text-anchor="end">VoltNestEnergy.com</text>
  </svg>
</main>
</body>
</html>
```